ZRD Roofing Billboard Design

Looking for a fresh new billboard design with my new headshot photo and using some info from my previous billboard and maybe website for design/content inspiration. My website is https://zrdroofing.com/

Also attached are my logo and current lawn sign design. I am looking for something simple, clean and modern. The landing page website should be 3816tops.com like my previous billboard has.

```html
<!DOCTYPE html>
<html lang="en">
<head>
<meta charset="UTF-8">
<title>ZRD Roofing Billboard</title>
<link href="https://fonts.googleapis.com/css2?family=Montserrat:wght@800;900&display=swap" rel="stylesheet">
<style>
  :root {
    --navy: #344a6f;
    --navy-deep: #1f2f52;
    --green: #69a851;
    --white: #ffffff;
    --shirt: #c9d3e6;
  }
  html, body {
    margin: 0;
    padding: 0;
    overflow: hidden;
  }
  .billboard {
    position: relative;
    width: 1200px;
    height: 364px;
    background: var(--navy);
    overflow: hidden;
    font-family: "Montserrat", Arial, sans-serif;
    font-weight: 800;
    color: var(--white);
  }
  .brand-mark {
    position: absolute;
    left: 80px;
    top: 25px;
    width: 130px;
    height: 130px;
    border-radius: 50%;
    border: 4px solid var(--white);
    box-sizing: border-box;
  }
  .brand-name {
    position: absolute;
    left: 0;
    width: 293px;
    top: 174px;
    margin: 0;
    text-align: center;
    font-size: 34px;
    line-height: 38px;
    letter-spacing: 0.5px;
  }
  .brand-rule {
    position: absolute;
    left: 59px;
    top: 262px;
    width: 176px;
    height: 2px;
    background: var(--green);
  }
  .brand-phone {
    position: absolute;
    left: 0;
    width: 293px;
    top: 276px;
    margin: 0;
    text-align: center;
    font-size: 34px;
    line-height: 38px;
    letter-spacing: 0.5px;
  }
  .headline {
    position: absolute;
    left: 306px;
    top: 24px;
    margin: 0;
    font-weight: 900;
    line-height: 1;
  }
  .headline-top {
    display: block;
    font-size: 88px;
    letter-spacing: 1px;
  }
  .headline-accent {
    display: block;
    margin-top: 8px;
    font-size: 62px;
    color: var(--green);
    letter-spacing: 0.5px;
  }
  .price-band {
    position: absolute;
    left: 307px;
    top: 184px;
    width: 585px;
    height: 71px;
  }
  .price-text {
    position: absolute;
    left: 331px;
    top: 199px;
    margin: 0;
    font-size: 43px;
    line-height: 43px;
    letter-spacing: 0.5px;
  }
  .site-url {
    position: absolute;
    left: 315px;
    top: 298px;
    margin: 0;
    font-size: 36px;
    line-height: 36px;
    letter-spacing: 0.5px;
  }
  .hero-visual {
    position: absolute;
    left: 706px;
    top: 0;
    width: 494px;
    height: 364px;
  }
</style>
</head>
<body>
<div class="billboard">
  <div class="brand-mark" aria-hidden="true"></div>
  <p class="brand-name">ZRD<br>ROOFING</p>
  <div class="brand-rule"></div>
  <p class="brand-phone">(860)<br>5550-127</p>

  <h1 class="headline">
    <span class="headline-top">FULL ROOF</span>
    <span class="headline-accent">REPLACEMENTS</span>
  </h1>

  <svg class="price-band" viewBox="0 0 585 71" aria-hidden="true">
    <path d="M40 0 H585 L535 71 H0 V40 A40 40 0 0 1 40 0 Z" fill="var(--green)"/>
  </svg>
  <p class="price-text">STARTING AT $7,499</p>

  <p class="site-url">3816TOPS.COM</p>

  <svg class="hero-visual" viewBox="0 0 494 364" role="img" aria-label="Smiling bearded man in a light blue shirt standing in front of a dark blue metal roof">
    <defs>
      <linearGradient id="roofTone" x1="0" y1="0" x2="1" y2="1">
        <stop offset="0" stop-color="#2a3d66"/>
        <stop offset="1" stop-color="#16223f"/>
      </linearGradient>
      <linearGradient id="personTone" x1="0" y1="0" x2="0" y2="1">
        <stop offset="0" stop-color="#8a6a58"/>
        <stop offset="0.45" stop-color="#b7c3da"/>
        <stop offset="1" stop-color="#c9d3e6"/>
      </linearGradient>
    </defs>
    <path d="M0 320 L120 210 L275 20 L494 110 V364 H10 Z" fill="url(#roofTone)"/>
    <path d="M135 364 C135 250 190 215 230 195 C235 120 250 20 330 12 C410 20 428 110 420 190 C470 215 494 240 494 250 V364 Z" fill="url(#personTone)"/>
  </svg>
</div>
</body>
</html>
```